Business Card Design Project - IT Company

Kestrafield Information Technology Solutions
We are an Information Technology Company. We provide computer services to commercial companies. We would like a new card full color front and back with bleeding edge.
We have a logo that you can use or if you want to come up with a new logo that is fine too.
Our colors are mostly Maroon and black but be creative.
Sample Information
Brent R Okafor
4812 W Saguaro Ridge Drive
Suite 820
Larkspur Vale, AZ 85390
O: 602.914.2037
C: 602.468.1290
24/7: 888.914.2037
bokafor@kestrafield.example
www.kestrafield.example
Target Market(s)
Business of all sizes
Industry/Entity Type
Computer
Requirements
Must have
- Bleeding edge
full color on both sides

```html
<!DOCTYPE html>
<html lang="en">
<head>
<meta charset="utf-8">
<title>Kestrafield Business Card</title>
<link rel="stylesheet" href="https://fonts.googleapis.com/css2?family=Open+Sans:ital,wght@0,400;0,700;1,700&family=Lato:wght@400&family=Tinos&display=swap">
<style>
  :root {
    --page: #ffffff;
    --red-deep: #c8202b;
    --red: #e81c26;
    --coral: #f07552;
    --coral-light: #f5a08a;
    --band: #ffffff;
    --logo-grey: #5d5e60;
    --sub-grey: #6f7073;
    --white: #ffffff;
    --title-grey: #d9d9db;
    --grey-dark: #8b8c8f;
    --grey-light: #dcdddf;
    --outline: #8a1f3c;
    --heading-red: #e8232c;
    --icon-a: #3b5b9a;
    --icon-b: #4bb3e0;
  }
  html, body { margin: 0; padding: 0; }
  body {
    width: 1200px; height: 1188px; overflow: hidden;
    background: var(--page); position: relative;
    font-family: "Open Sans", Arial, sans-serif;
  }
  .card {
    position: absolute; left: 273px; width: 615px; height: 352px;
    border-radius: 26px; overflow: hidden;
  }
  .card-front { top: 184px; }
  .card-back { top: 574px; left: 272px; }
  .card-art { position: absolute; inset: 0; }
  .brand-band {
    position: absolute; left: 0; top: 35px; width: 615px; height: 82px;
    background: var(--band);
  }
  .brand-name {
    position: absolute; left: 145px; top: 6px;
    font-family: "Lato", Arial, sans-serif; font-weight: 400;
    font-size: 44px; letter-spacing: 6px; line-height: 1;
    color: var(--logo-grey); margin: 0;
  }
  .brand-tagline {
    position: absolute; left: 146px; top: 54px;
    font-family: "Tinos", "Times New Roman", serif;
    font-size: 22.5px; color: var(--sub-grey); margin: 0; line-height: 1;
  }
  .holder-name {
    position: absolute; right: 41px; top: 258px; margin: 0;
    font-weight: 700; font-style: italic; font-size: 33px;
    color: var(--white); line-height: 1;
  }
  .holder-title {
    position: absolute; right: 51px; top: 298px; margin: 0;
    font-weight: 700; font-style: italic; font-size: 24px;
    color: var(--title-grey); line-height: 1;
  }
  .back-heading {
    position: absolute; left: 40px; top: 36px; margin: 0;
    font-weight: 700; font-size: 25.5px; color: var(--heading-red);
    -webkit-text-stroke: 0.6px var(--white);
    text-shadow: 0 0 2px rgba(255,255,255,0.9);
    letter-spacing: 0; line-height: 1;
  }
  .contact { position: absolute; left: 37px; margin: 0; color: var(--white); font-size: 19px; line-height: 26.5px; }
  .contact-address { top: 98px; }
  .contact-phones { top: 182px; }
  .contact-web { top: 269px; }
  .social { position: absolute; top: 287px; left: 497px; display: flex; gap: 6px; }
  .social-square { width: 34px; height: 34px; border-radius: 5px; }
  .social-square.one { background: var(--icon-a); }
  .social-square.two { background: var(--icon-b); }
</style>
</head>
<body>

<section class="card card-front">
  <svg class="card-art" width="615" height="352" viewBox="0 0 615 352" aria-hidden="true">
    <defs>
      <linearGradient id="frontBase" x1="0" y1="0" x2="1" y2="1">
        <stop offset="0" stop-color="var(--red-deep)"/>
        <stop offset="0.55" stop-color="var(--red)"/>
        <stop offset="1" stop-color="#ef3d35"/>
      </linearGradient>
      <linearGradient id="frontSweep" x1="0" y1="0" x2="1" y2="1">
        <stop offset="0" stop-color="var(--coral)"/>
        <stop offset="0.5" stop-color="var(--coral)"/>
        <stop offset="1" stop-color="var(--coral-light)"/>
      </linearGradient>
    </defs>
    <rect width="615" height="352" fill="url(#frontBase)"/>
    <path d="M37 352 Q410 300 512 0 L615 0 L615 352 Z" fill="url(#frontSweep)"/>
  </svg>
  <div class="brand-band">
    <p class="brand-name">KESTRAFIELD</p>
    <p class="brand-tagline">Information Technology Solutions</p>
  </div>
  <h1 class="holder-name">Brent R Okafor</h1>
  <p class="holder-title">CEO</p>
</section>

<section class="card card-back">
  <svg class="card-art" width="615" height="352" viewBox="0 0 615 352" aria-hidden="true">
    <defs>
      <linearGradient id="backBase" x1="0" y1="0" x2="1" y2="1">
        <stop offset="0" stop-color="var(--grey-dark)"/>
        <stop offset="1" stop-color="var(--grey-light)"/>
      </linearGradient>
      <linearGradient id="backSweep" x1="0" y1="0" x2="1" y2="1">
        <stop offset="0" stop-color="#aeafb2"/>
        <stop offset="1" stop-color="#d6d7d9"/>
      </linearGradient>
    </defs>
    <rect width="615" height="352" fill="url(#backBase)"/>
    <path d="M91 0 Q150 330 566 352 L0 352 L0 0 Z" fill="url(#backSweep)"/>
    <rect x="0.5" y="0.5" width="614" height="351" rx="26" fill="none" stroke="var(--outline)" stroke-width="1.2"/>
  </svg>
  <h2 class="back-heading">INFORMATION TECHNOLOGY SOLUTIONS</h2>
  <p class="contact contact-address">4812 W Saguaro Ridge Drive<br>Suite 820<br>Larkspur Vale, AZ 85390</p>
  <p class="contact contact-phones">O: 602.914.2037<br>C: 602.468.1290<br>24/7: 888.914.2037</p>
  <p class="contact contact-web">bokafor@kestrafield.example<br>www.kestrafield.example</p>
  <div class="social" role="img" aria-label="Social network links">
    <div class="social-square one"></div>
    <div class="social-square two"></div>
  </div>
</section>

</body>
</html>
```